author needs a Book Cover design

Needs a book cover design that matches the title in some way.
Book Title is- 9 Lanterns Beneath a Quiet Harbor Tonight.
Subtile- Harvest Lessons Across Ordinary Seasons.
Author Name:-Desmond Okorefe, Jr.

Final Design is subject to Book Publisher's requirement.

Font styles to use
Serif

Requirements
Must have
• Follow these recommended specifications for your cover file:
• Page Size: Your cover should be a single (one-piece) PDF that includes the back cover, spine, and front cover. You can submit your cover on any size page as long as the printable area is measured exactly for your book's trim size, spine width, and allows at least .125” bleed, centered horizontally and vertically.
• Minimum Cover Width: Bleed + Back Cover Trim Size + Spine Width + Front Cover Trim Size + Bleed
• Minimum Cover Height: Bleed + Book Height Trim Size + Bleed
• Trim Size: Your cover should be the same trim size as you choose in the Title Information when setting up your book. For example, submitting a cover that was previously used for a 6.25” x 9.25” book would not work for a 6” x 9” book.
• Barcodes: For manufacturing and distribution reasons, your book's back cover must include a valid ISBN barcode. If your cover already has an ISBN barcode, make sure it is high-resolution, or at least 300 dpi, and 1.5" - 2" in width with proportional height. Ideally, this barcode should be 2” wide by 1.2” tall. Also, check to make sure you have the rights to use the ISBN on your cover, because not all services allow you to use their ISBNs elsewhere.
• QR codes: There are no set size restrictions, but the quality (resolution) of the image must be set to at least 300 dpi. Make sure you have the rights to use the code.
• If your artwork does not include a barcode, we will automatically add one in the lower right-hand corner of your book's back cover, free of charge. Our system will place the ISBN barcode in a space 2" wide and 1.2" tall. The bottom of this barcode is located 1/4" up from the bottom trim line of the cover. The right side of the barcode is located 1/4" to the left of the spine. Please ensure that you don't have any important images or text in the barcode location. You can also refer to our Artwork Templates for the exact size and position of the ISBN barcode on your final cover.
• If you don’t have an ISBN already on your cover, but you have live graphic or text elements in the location that our system will place the ISBN, you will need to move those elements or place the ISBN in a different location yourself.
• Publishing Logos: We do not add our logo to your book.
• Spine Width and Variance: If your artwork was created for a different service, please make sure that the spine width of your current cover matches our spine width. Different services may use different paper thickness, which is why the spine width of your cover artwork could be correct for another service but incorrect for our service.
• Ideally, you should avoid hard vertical lines separating your front or back cover panels from your spine and should allow for at least a .125" variance of your spine on each side (for example, the text on a 1" spine should be no larger than .75" wide). For books with a page count of less than 130 pages, we strongly recommend a blank spine.
• Your spine width should be calculated based on the number of pages in your book and using the appropriate formula:
• Black and White Interior Book Spine Width:
• White paper: Number of pages x .002252 = Spine width in inches
• Cream paper: Number of pages x .0025 = Spine width in inches
• Color Interior Book Spine Width:
• Number of pages x .002347 = Spine width in inches
• Example of spine width calculation for a 120-page black and white interior book with white paper:
• 120 x .002252 = .27" spine width
• Text and Image Placement: All live cover elements, or text and images that cannot be cut, must be at least .125" inside the trim lines to ensure no important elements are cut during the bookmaking process and the appearance of your printed books is consistent.
• Bleed: Your cover's background must extend at least .125" beyond the final trim line to accommodate for cutting/trimming tolerance.
• Crop/Registration Marks: Please do not include any crop or registration marks on your files, as they may interfere with the binding process or appear on the cover. We use our own measurements, specific to our systems, for cutting and binding; crop or registration marks placed by you could interfere with this process.
• Images and Fonts: Any images you include on your book's cover may be tagged with your choice of CMYK or RGB profiles or left untagged in a generic color space. All images should be sized at 100%, flattened to one layer and placed in your native document at a resolution of at least 300 DPI. You should also embed all fonts in your PDF file.
• Desmond, I hope this information is helpful to you. Please feel free to contact us if you have any other questions or concerns.
• Best regards,
• *WILL SUPPLY THE PAGE NUMBERS INFORMATION
• Lisbeth
• PrintHollow Member Services
Nice to have
• An attractive design that matches the title. Design can include backgrounds

```html
<!DOCTYPE html>
<html lang="en">
<head>
<meta charset="utf-8">
<title>9 Lanterns Beneath a Quiet Harbor Tonight — Cover</title>
<link rel="stylesheet" href="https://fonts.googleapis.com/css2?family=Bebas+Neue&family=Oswald:wght@500;700&family=Cinzel:wght@400;600&display=swap">
<style>
  :root {
    --page-bg: #f2f2f2;
    --cover-bg: #3b3a3b;
    --title-red: #8e1316;
    --title-grey: #a3a3a3;
    --text-white: #f4f4f4;
    --art-light: #bdbdbd;
    --art-dark: #4a494a;
  }
  * { margin: 0; padding: 0; box-sizing: border-box; }
  html, body {
    width: 1200px;
    height: 1059px;
    overflow: hidden;
    background: var(--page-bg);
  }
  .cover {
    position: absolute;
    left: 300px;
    top: 80px;
    width: 600px;
    height: 900px;
    background: var(--cover-bg);
    box-shadow: 0 12px 40px rgba(0,0,0,0.25);
    overflow: hidden;
  }
  .subtitle {
    position: absolute;
    top: 58px;
    left: 0;
    width: 100%;
    text-align: center;
    font-family: "Bebas Neue", sans-serif;
    color: var(--text-white);
    white-space: nowrap;
    letter-spacing: 0.5px;
  }
  .subtitle .minor { font-size: 28px; }
  .subtitle .major { font-size: 38px; }
  .title-numeral {
    position: absolute;
    top: 112px;
    left: 34px;
    font-family: "Oswald", sans-serif;
    font-weight: 700;
    font-size: 250px;
    line-height: 1;
    color: var(--title-red);
  }
  .title-lanterns {
    position: absolute;
    top: 148px;
    left: 170px;
    font-family: "Oswald", sans-serif;
    font-weight: 500;
    font-size: 92px;
    line-height: 1;
    color: var(--title-grey);
    letter-spacing: 1px;
  }
  .title-connector {
    position: absolute;
    top: 262px;
    left: 172px;
    font-family: "Oswald", sans-serif;
    font-weight: 500;
    font-size: 26px;
    line-height: 1;
    color: var(--text-white);
    letter-spacing: 2px;
  }
  .title-harbor {
    position: absolute;
    top: 292px;
    left: 126px;
    font-family: "Cinzel", serif;
    font-weight: 600;
    font-size: 100px;
    line-height: 1;
    color: var(--title-red);
  }
  .title-tonight {
    position: absolute;
    top: 410px;
    left: 0;
    width: 100%;
    text-align: center;
    font-family: "Bebas Neue", sans-serif;
    font-size: 58px;
    line-height: 1;
    color: var(--text-white);
    letter-spacing: 1px;
  }
  .cover-art {
    position: absolute;
    top: 540px;
    left: 0;
    width: 100%;
    height: 250px;
  }
  .author {
    position: absolute;
    bottom: 46px;
    left: 0;
    width: 100%;
    text-align: center;
    font-family: "Cinzel", serif;
    font-size: 32px;
    color: var(--text-white);
    letter-spacing: 1px;
  }
</style>
</head>
<body>
  <main class="cover">
    <p class="subtitle">
      <span class="minor">HARVEST</span>
      <span class="major">LESSONS</span>
      <span class="minor">ACROSS</span>
      <span class="major">ORDINARY SEASONS</span>
    </p>

    <h1 class="title">
      <span class="title-numeral">9</span>
      <span class="title-lanterns">LANTERNS</span>
      <span class="title-connector">BENEATH A QUIET</span>
      <span class="title-harbor">HARBOR</span>
      <span class="title-tonight">TONIGHT</span>
    </h1>

    <svg class="cover-art" viewBox="0 0 600 250" role="img" aria-label="Grey line illustration of a winged figure reaching toward a running hare along the ground">
      <defs>
        <linearGradient id="art-fade" x1="0" y1="0" x2="1" y2="0">
          <stop offset="0" stop-color="var(--art-light)" stop-opacity="0.55"/>
          <stop offset="0.6" stop-color="var(--art-light)" stop-opacity="0.25"/>
          <stop offset="1" stop-color="var(--art-dark)" stop-opacity="0.2"/>
        </linearGradient>
      </defs>
      <rect x="0" y="0" width="600" height="250" fill="url(#art-fade)"/>
      <line x1="0" y1="232" x2="600" y2="248" stroke="var(--art-light)" stroke-width="2"/>
    </svg>

    <p class="author">DESMOND OKOREFE, JR.</p>
  </main>
</body>
</html>
```